Larvik Consulting

Hi,
I have my own network consulting business (just me)
and need to get a logo and business card design together,

Based in New Zealand,

Tobias Wrenfield
Unified Communications and Network Architect

/design engineer,
and would like this to be the basis for personal branding and company identity

Industry/Entity Type

Business

Requirements
Nice to have
• I have the basis for a optional logo - needs color -

```html
<!DOCTYPE html>
<html lang="en">
<head>
<meta charset="utf-8">
<title>Larvik Consulting – Business Card</title>
<link rel="stylesheet" href="https://fonts.googleapis.com/css2?family=Titillium+Web:ital,wght@0,400;0,600;0,700;1,700&family=Open+Sans:wght@400&display=swap">
<style>
  :root {
    --page-bg: #6a6a6a;
    --card-blue-light: #1f6fa6;
    --card-blue: #0d5389;
    --card-blue-dark: #063c66;
    --band-grey: #474747;
    --accent-cyan: #4fc3ea;
    --text-white: #ffffff;
    --text-soft: #d6d6d6;
    --tagline: #0a3456;
    --tagline-back: #a9c7dd;
  }
  * { box-sizing: border-box; margin: 0; padding: 0; }
  html, body {
    width: 1200px;
    height: 800px;
    overflow: hidden;
  }
  body {
    background: var(--page-bg);
    display: flex;
    align-items: center;
    justify-content: center;
    gap: 40px;
    font-family: "Open Sans", Arial, sans-serif;
  }
  .card {
    position: relative;
    width: 540px;
    height: 309px;
    overflow: hidden;
    background: radial-gradient(ellipse 70% 80% at 22% 28%, var(--card-blue-light) 0%, var(--card-blue) 45%, var(--card-blue-dark) 100%);
    box-shadow: 0 10px 24px rgba(0,0,0,0.35);
  }

  /* Front */
  .brand {
    position: absolute;
    left: 70px;
    top: 62px;
    display: flex;
    align-items: center;
    gap: 14px;
  }
  .brand-dot {
    width: 34px;
    height: 34px;
    border-radius: 50%;
    background: var(--accent-cyan);
  }
  .brand-name {
    font-family: "Titillium Web", Arial, sans-serif;
    font-weight: 700;
    font-size: 27px;
    line-height: 1;
    color: var(--text-white);
  }
  .brand-tagline {
    position: absolute;
    left: 118px;
    top: 98px;
    font-size: 11px;
    color: var(--tagline);
  }
  .info-band {
    position: absolute;
    left: 0;
    right: 0;
    bottom: 0;
    height: 116px;
    background: var(--band-grey);
  }
  .person {
    position: absolute;
    right: 22px;
    top: 168px;
    text-align: right;
    font-family: "Titillium Web", Arial, sans-serif;
  }
  .person-name {
    font-weight: 600;
    font-size: 19px;
    line-height: 1.1;
    color: var(--accent-cyan);
  }
  .person-title {
    font-weight: 700;
    font-style: italic;
    font-size: 14px;
    line-height: 1.1;
    color: var(--text-white);
  }
  .person-role {
    margin-top: 10px;
    font-family: "Open Sans", Arial, sans-serif;
    font-size: 12px;
    color: var(--text-white);
  }
  .contact {
    position: absolute;
    left: 24px;
    bottom: 18px;
    font-size: 10.5px;
    line-height: 1.5;
    color: var(--text-soft);
  }

  /* Back */
  .card-back {
    background: radial-gradient(ellipse 45% 60% at 50% 38%, var(--card-blue-light) 0%, var(--card-blue) 50%, var(--card-blue-dark) 100%);
  }
  .back-brand {
    position: absolute;
    left: 0;
    right: 0;
    top: 92px;
    display: flex;
    flex-direction: column;
    align-items: center;
    gap: 14px;
  }
  .back-brand .brand-dot {
    width: 48px;
    height: 48px;
  }
  .back-brand .brand-name { font-size: 24px; }
  .back-tagline {
    margin-top: -12px;
    font-size: 10.5px;
    color: var(--tagline-back);
  }
</style>
</head>
<body>
  <section class="card card-front">
    <div class="brand">
      <span class="brand-dot"></span>
      <span class="brand-name">Larvik Consulting</span>
    </div>
    <p class="brand-tagline">network consulting business</p>
    <div class="info-band"></div>
    <div class="person">
      <p class="person-name">Tobias Wrenfield</p>
      <p class="person-title">design engineer</p>
      <p class="person-role">Unified Communications &amp; Network Architect</p>
    </div>
    <div class="contact">
      <p>mobile: (400)mobile number</p>
      <p>email: youremail@domain.com</p>
    </div>
  </section>

  <section class="card card-back">
    <div class="back-brand">
      <span class="brand-dot"></span>
      <span class="brand-name">Larvik Consulting</span>
      <span class="back-tagline">network consulting business</span>
    </div>
  </section>
</body>
</html>
```